Design a box or sticker to be placed onto of a box for sports cards & other collectibles

We are starting up a business to sell limited edition sports collectibles, such as signed cards, jerseys, figurines etc online. Please refer to the blue box for reference on how the shape of the box will look like .

Design opaque stickers of GCA, Baseball, Football, Basketball, Vela Tides & KPR with a silhoutte/edgy feel to them.

Example: silhouette of a player playing the sports and the sport's ball or equipment to be coloured will look minimalistic and sleek. (For example: black figure with orange basket ball).

To ensure all our changes have been met. The GCA foil design is still not changed to look the same as the GCA sticker design.

Target Market(s)

Sports fans (basketball, soccer, football, baseball, wrestling etc), and collectible enthusiasts

Font styles to use
Other font styles liked:
• fonts should give off a "sporty" feel

Requirements
Must have
• Company logo without background (please remove the background), sleek design. The background colour is our company logo. +points if you are able to tastefully incorporate it into the design.
Nice to have
• open to discussion
Should not have
• open to discussion

```html
<!DOCTYPE html>
<html lang="en">
<head>
<meta charset="utf-8">
<title>Torvane HCL Legends Collector Box</title>
<link rel="stylesheet" href="https://fonts.googleapis.com/css2?family=Oswald:wght@700&family=Kaushan+Script&family=Fira+Sans+Condensed:wght@700&family=Marcellus&display=swap">
<style>
  :root {
    --canvas: #ffffff;
    --lid: #8c6dbe;
    --box-body: #7a58b2;
    --band-black: #000000;
    --band-purple: #4f1f98;
    --card-deep: #241055;
    --card-mid: #4b2a95;
    --photo-light: #8a6ccc;
    --accent-blue: #1e90ff;
    --accent-orange: #f6a21a;
    --text-light: #ffffff;
  }
  html, body {
    margin: 0;
    padding: 0;
    width: 900px;
    height: 1200px;
    overflow: hidden;
    background: var(--canvas);
  }
  .canvas {
    position: relative;
    width: 900px;
    height: 1200px;
  }
  .box-view, .sticker-view {
    position: absolute;
    left: 0;
    top: 0;
  }
  .lid-brand {
    font-family: "Marcellus", serif;
    fill: var(--text-light);
    font-size: 46px;
    letter-spacing: 1px;
  }
  .card-legend-word { font-family: "Kaushan Script", cursive; fill: var(--accent-orange); }
  .card-league { font-family: "Oswald", sans-serif; font-weight: 700; fill: var(--text-light); }
  .card-tagline { font-family: "Fira Sans Condensed", sans-serif; font-weight: 700; fill: var(--text-light); }
  .card-brand { font-family: "Marcellus", serif; fill: var(--text-light); }
</style>
</head>
<body>
<main class="canvas">
  <svg width="0" height="0" style="position:absolute" aria-hidden="true">
    <defs>
      <linearGradient id="card-bg" x1="0" y1="0" x2="0" y2="1">
        <stop offset="0" stop-color="#5a3aa8"/>
        <stop offset="1" stop-color="#2a1262"/>
      </linearGradient>
      <linearGradient id="photo-fill" x1="0" y1="0" x2="1" y2="1">
        <stop offset="0" stop-color="#7a5cc4"/>
        <stop offset="0.6" stop-color="#4d2e98"/>
        <stop offset="1" stop-color="#2c1468"/>
      </linearGradient>
      <linearGradient id="figure-fill" x1="0" y1="0" x2="1" y2="1">
        <stop offset="0" stop-color="#0a0a1a"/>
        <stop offset="1" stop-color="#1aa6e0"/>
      </linearGradient>
      <symbol id="collector-card" viewBox="0 0 227 305">
        <rect class="card-base" width="227" height="305" fill="url(#card-bg)"/>
        <rect class="card-photo" x="0" y="0" width="227" height="230" fill="url(#photo-fill)" opacity="0.9" role="img" aria-label="Basketball action photo of players leaping at the hoop in a crowded arena"/>
        <polygon class="card-stripe" points="0,120 0,305 40,305 130,90 90,60" fill="#1b0b45" opacity="0.55"/>
        <polygon class="card-stripe" points="227,180 227,305 150,305" fill="#160838" opacity="0.7"/>
        <polygon class="card-stripe" points="0,225 0,305 60,305 85,225" fill="#1a0c48"/>
        <polygon class="card-accent-light" points="95,165 135,165 110,225 70,225" fill="#2a6fe0"/>
        <polygon class="card-accent" points="110,165 138,165 118,218 88,218" fill="var(--accent-blue)"/>
        <rect class="card-figure" x="38" y="88" width="72" height="100" rx="6" fill="url(#figure-fill)" role="img" aria-label="Silhouette of a basketball player leaping with the ball"/>
        <text class="card-league" x="90" y="163" font-size="36">HCL</text>
        <text class="card-legend-word" x="108" y="178" font-size="21" transform="rotate(-8 130 172)">Legends</text>
        <text class="card-tagline" x="101" y="221" font-size="12.5">Collector Cards</text>
        <text class="card-brand" x="113.5" y="282" font-size="38" text-anchor="middle">TORVANE</text>
        <rect class="card-frame" x="1" y="1" width="225" height="303" fill="none" stroke="#dcd4f0" stroke-width="1.5"/>
      </symbol>
    </defs>
  </svg>

  <svg class="box-view" width="900" height="600" viewBox="0 0 900 600">
    <polygon class="box-lid" points="267,45 656,45 725,235 198,235" fill="var(--lid)"/>
    <text class="lid-brand" x="462" y="150" text-anchor="middle">TORVANE</text>
    <rect class="box-front" x="198" y="235" width="527" height="361" fill="var(--box-body)"/>
    <rect class="band-dark" x="315" y="235" width="143" height="361" fill="var(--band-black)"/>
    <rect class="band-purple" x="458" y="235" width="147" height="361" fill="var(--band-purple)"/>
    <use href="#collector-card" x="339" y="255" width="245" height="323"/>
  </svg>

  <svg class="sticker-view" width="900" height="1200" viewBox="0 0 900 1200" style="pointer-events:none">
    <rect class="band-dark" x="192" y="627" width="266" height="537" fill="var(--band-black)"/>
    <rect class="band-purple" x="458" y="627" width="267" height="537" fill="var(--band-purple)"/>
    <use href="#collector-card" x="294" y="668" width="341" height="457"/>
  </svg>
</main>
</body>
</html>
```